Medical equipment business looking for professional, unique business card

We need a business card design for a durable medical equipment company. We are small but would like our cards to express that we are much bigger. We focus on braces (back, knee, wrist, etc) but also do crutches, rollators, wheelchairs- basically medical equipment that gets you going and back in Action. Our colors are blue and green and our logo has an arrow and use of a "spine". We'd like to express professionalism while being unique.

Industry/Entity Type

Medical Equipment

Contact Information for Business Card

Professional feel but unique. Memorable.

Font styles to use
Serif
Sans Serif
Other font styles liked:
• verdana

Requirements
Must have
• card holders cell#, business phone#, fax#, email, website address, business address, logo
Nice to have
• use of medical/healthcare related descriptive words, items, look
Should not have
• the wrong colors or cartoon characters.

```html
<!DOCTYPE html>
<html lang="en">
<head>
<meta charset="utf-8">
<title>Stride Medical – Business Card</title>
<link rel="stylesheet" href="https://fonts.googleapis.com/css2?family=Noto+Sans:wght@400;700;800&family=Roboto+Condensed:wght@400&display=swap">
<style>
  :root {
    --navy: #0b4168;
    --wave-blue: #1a86c7;
    --lime: #8cc63f;
    --paper: #ffffff;
    --backdrop: #e9e9ea;
    --ink: #0b4168;
    --soft-white: #dfe8f0;
  }
  * { margin: 0; padding: 0; box-sizing: border-box; }
  html, body {
    width: 927px; height: 1200px; overflow: hidden;
    background: var(--backdrop);
  }
  .stage {
    position: relative; width: 927px; height: 1200px;
    display: flex; align-items: center; justify-content: center;
  }
  .business-card {
    position: relative; width: 820px; height: 468px;
    background: var(--paper);
    box-shadow: 0 18px 36px rgba(0,0,0,0.18);
    overflow: hidden;
  }
  .card-art { position: absolute; inset: 0; width: 100%; height: 100%; }
  .brand {
    position: absolute; left: 66px; top: 78px;
    display: flex; align-items: center; gap: 12px;
  }
  .brand-dot {
    width: 18px; height: 18px; border-radius: 50%;
    background: var(--lime);
  }
  .brand-name {
    font-family: "Noto Sans", Verdana, sans-serif;
    font-weight: 700; font-size: 38px; color: var(--paper);
    letter-spacing: -0.5px;
  }
  .holder {
    position: absolute; left: 62px; top: 282px;
    color: var(--paper);
    font-family: "Noto Sans", Verdana, sans-serif;
  }
  .holder-name { font-weight: 800; font-size: 34px; line-height: 1.1; }
  .holder-title {
    margin-top: 6px; font-weight: 400; font-size: 16px;
    letter-spacing: 5px; color: var(--soft-white);
  }
  .contact {
    position: absolute; right: 40px; top: 100px;
    text-align: right; color: var(--ink);
    font-family: "Roboto Condensed", "Arial Narrow", sans-serif;
    font-size: 23px; line-height: 31px;
  }
  .contact-group + .contact-group { margin-top: 34px; }
  .contact-label { margin-right: 10px; }
</style>
</head>
<body>
<main class="stage">
  <article class="business-card">
    <svg class="card-art" viewBox="0 0 757 432" preserveAspectRatio="none" aria-hidden="true">
      <path d="M459 0 C452 70 476 130 472 215 C468 300 454 370 458 432 H0 V0 Z" fill="var(--wave-blue)"/>
      <path d="M453 0 C446 70 469 130 465 215 C461 300 448 370 452 432 H0 V0 Z" fill="var(--navy)"/>
      <g fill="var(--lime)">
        <circle cx="432" cy="22" r="7"/>
        <circle cx="426" cy="57" r="7"/>
        <circle cx="423" cy="94" r="7"/>
        <circle cx="424" cy="129" r="7"/>
        <circle cx="426" cy="164" r="7"/>
        <circle cx="431" cy="200" r="7"/>
        <circle cx="437" cy="235" r="7"/>
        <circle cx="442" cy="270" r="7"/>
        <circle cx="445" cy="306" r="7"/>
        <circle cx="445" cy="342" r="7"/>
        <circle cx="444" cy="378" r="7"/>
        <circle cx="437" cy="414" r="7"/>
      </g>
    </svg>

    <div class="brand">
      <span class="brand-dot"></span>
      <span class="brand-name">Stride Medical</span>
    </div>

    <div class="holder">
      <h1 class="holder-name">Daniel Harwick</h1>
      <p class="holder-title">MEDICAL ENGINEER</p>
    </div>

    <address class="contact" style="font-style: normal;">
      <div class="contact-group">
        <div>418 W. Alder Street</div>
        <div>Fresno, CA 93721</div>
      </div>
      <div class="contact-group">
        <div><span class="contact-label">p.</span>559-410-2286</div>
        <div><span class="contact-label">f.</span>559-410-2286</div>
      </div>
      <div class="contact-group">
        <div>daniel@stridemedical.com</div>
        <div>www.stridemedical.com</div>
      </div>
    </address>
  </article>
</main>
</body>
</html>
```